Office and banking equipment supplier needs a company profile/products catalogue

we need a profile/products catalog design for our company. we are specialized in banking and office related equipment. we have an old design but we need a new refined one. I'm attaching the old one (a higher resolution one can be sent through we transfer) where the products' images are up to date, yet the design is no convincing. the new catalog should have a noticeable identity, properly executed and descriptive with minimal text. the old one is quite big but it has all of the products listed in it. with a description of each category. however, the designer is free to add, amend or delete whatever he/she thinks suitable to grab the attention of the reader.

Reason: Still waiting some designs.

Target Market(s)

Banks, Education sectors, Office Automation, Government

Industry/Entity Type

Office Furniture

Font styles to use
Serif

Requirements
Must have
• lifetime design, excellent point of entry, eye catching design that directs the customer towards the product, intergartion
Nice to have
• Catalog copy must be clear, concise, easy to read, educational or even entertaining. The catalog user must be teased to ask about more information required to make a purchase decision, or risk losing the sale. Ordering information and pricing should be presented in easy to read tables.
• it must be visual, allowing the user to breeze through with minimal effort. Photography supports the visual experience.
• a good info graphic about the company.
Should not have
• dull designs.

```html
<!DOCTYPE html>
<html lang="en">
<head>
<meta charset="utf-8">
<title>Karvo Office Systems — Catalogue Cover Spread</title>
<link rel="stylesheet" href="https://fonts.googleapis.com/css2?family=Open+Sans:wght@400;700&family=PT+Serif:wght@700&family=Amiri:wght@700&display=swap">
<style>
  :root {
    --backdrop: #ececef;
    --paper: #f4f4f5;
    --paper-grey: #dcdcdf;
    --brand-blue: #1f2f8f;
    --photo-violet-light: #7d7fae;
    --photo-violet-mid: #5b5c90;
    --photo-violet-dark: #3a2e55;
    --ink: #1b1b1f;
    --white: #ffffff;
  }
  * { margin: 0; padding: 0; box-sizing: border-box; }
  html, body {
    width: 1200px;
    height: 880px;
    overflow: hidden;
    background: var(--backdrop);
  }
  .spread {
    position: absolute;
    left: 40px;
    top: 120px;
    width: 1120px;
    height: 640px;
    display: flex;
    box-shadow: 0 10px 30px rgba(0,0,0,0.12);
  }
  .panel {
    position: relative;
    width: 560px;
    height: 640px;
    overflow: hidden;
  }
  .panel svg.panel-art {
    position: absolute;
    inset: 0;
  }
  .back-cover {
    background: linear-gradient(160deg, #e6e6e9 0%, var(--paper-grey) 100%);
    border-right: 1px solid rgba(0,0,0,0.08);
  }
  .front-cover {
    background: var(--paper);
  }
  .website {
    position: absolute;
    left: 22px;
    top: 32px;
    font-family: "Open Sans", sans-serif;
    font-size: 11px;
    font-weight: 700;
    color: var(--brand-blue);
    letter-spacing: 0.2px;
  }
  .tagline {
    position: absolute;
    left: 330px;
    top: 40px;
    width: 210px;
    font-family: "Open Sans", sans-serif;
    font-size: 18px;
    line-height: 1.35;
    color: var(--white);
  }
  .brand-block {
    position: absolute;
    left: 28px;
    top: 56px;
    width: 250px;
  }
  .brand-mark {
    display: flex;
    align-items: center;
    gap: 10px;
    font-family: "Open Sans", sans-serif;
    font-weight: 700;
    font-size: 38px;
    color: var(--brand-blue);
    line-height: 1;
  }
  .brand-dot {
    width: 20px;
    height: 20px;
    border-radius: 50%;
    background: var(--brand-blue);
  }
  .company-name {
    margin-top: 18px;
    font-family: "PT Serif", serif;
    font-weight: 700;
    font-size: 14px;
    color: var(--ink);
    white-space: nowrap;
  }
  .company-name small {
    font-size: 9px;
  }
  .company-name-ar {
    margin-top: 2px;
    font-family: "Amiri", serif;
    font-weight: 700;
    font-size: 15px;
    color: var(--ink);
    direction: rtl;
    text-align: left;
  }
</style>
</head>
<body>
  <main class="spread">
    <section class="panel back-cover">
      <svg class="panel-art" width="560" height="640" viewBox="0 0 560 640">
        <defs>
          <linearGradient id="vault-tone" x1="0" y1="0" x2="1" y2="1">
            <stop offset="0" stop-color="var(--photo-violet-light)"/>
            <stop offset="1" stop-color="var(--photo-violet-mid)"/>
          </linearGradient>
        </defs>
        <path role="img" aria-label="Photograph of a bank vault with rows of safe deposit boxes"
              d="M200,0 H560 V560 C380,530 220,340 200,0 Z" fill="url(#vault-tone)"/>
        <path d="M200,0 C220,340 380,530 560,560" fill="none" stroke="var(--brand-blue)" stroke-width="9"/>
      </svg>
      <p class="website">www.karvo-systems.com</p>
    </section>

    <section class="panel front-cover">
      <svg class="panel-art" width="560" height="640" viewBox="0 0 560 640">
        <defs>
          <linearGradient id="coins-tone" x1="0" y1="0" x2="1" y2="1">
            <stop offset="0" stop-color="var(--photo-violet-dark)"/>
            <stop offset="0.6" stop-color="#4b3f68"/>
            <stop offset="1" stop-color="var(--photo-violet-mid)"/>
          </linearGradient>
        </defs>
        <path role="img" aria-label="Close-up photograph of stacked coins on a reflective table"
              d="M300,0 H560 V570 C420,550 310,340 300,0 Z" fill="url(#coins-tone)"/>
        <path d="M300,0 C310,340 420,550 560,570" fill="none" stroke="var(--brand-blue)" stroke-width="9"/>
      </svg>
      <p class="tagline">Karvo is a leading supplier of banking and office related equipment.</p>
      <div class="brand-block">
        <div class="brand-mark"><span class="brand-dot"></span>KARVO</div>
        <p class="company-name">KARVO OFFICE SYSTEMS <small>CO. LTD.</small></p>
        <p class="company-name-ar">شركة كارفو للأنظمة المكتبية</p>
      </div>
    </section>
  </main>
</body>
</html>
```